Design AND code an HTML landing page

A landing page for campaigns and webinars respondents for project www.brevamor-homes.example. We expect the design to be coded. We will provide the copy and content. It will be a simple landing page for a new development project, to capture details of any potential clients showing interest, including any leads generated via webinars.

Broad instructions are as follows:
- It should not have a header or footer. Minimum escape links as possible.
- Create a lead generator box to get e-mails / relevant info of people interested.
- If possible, add a virtual tour (link to host server provided) at the top of the page.
- Content will be provided
- An option to include a link to a ClipVerra video

Target Market(s)

Pre/retiree and retirees

Industry/Entity Type

Real estate development, retirement, relocation, travel and tourism

Coding

Coded - Design and coding required

Font styles to use
Other font styles liked:
• Preferably same as existing site

Colors
FFF300
FFF600
FEFA6F
FFFEC7
FFFEE8

Requirements
Must have
• Simple yet appealing look and feel, within the motif of the project, simple list of questions
Should not have
• Emojis, unrelated graphics, excessive graphics that are not linked to project

```html
<!DOCTYPE html>
<html lang="en">
<head>
<meta charset="utf-8">
<title>Brevamor Living – Reinventing Retirement</title>
<link href="https://fonts.googleapis.com/css2?family=Work+Sans:wght@400;500;600&display=swap" rel="stylesheet">
<style>
  :root {
    --brand-yellow: #FFDD00;
    --ink: #111111;
    --white: #FFFFFF;
    --hero-top: #1d2736;
    --hero-mid: #2f3433;
    --hero-bottom: #3a3b33;
    --rule: #9a9a9a;
  }
  * { box-sizing: border-box; margin: 0; padding: 0; }
  html, body {
    width: 1200px;
    height: 708px;
    overflow: hidden;
    background: var(--white);
    font-family: "Work Sans", Arial, sans-serif;
    color: var(--ink);
  }
  .page { position: relative; width: 1200px; height: 708px; }

  .hero {
    position: absolute;
    left: 0; top: 0;
    width: 1200px; height: 542px;
    background:
      radial-gradient(ellipse at 50% 60%, rgba(90,90,80,0.35), transparent 60%),
      linear-gradient(180deg, var(--hero-top) 0%, var(--hero-mid) 55%, var(--hero-bottom) 100%);
  }
  .hero-actions {
    position: absolute;
    top: 19px; left: 984px;
    display: flex; gap: 8px;
  }
  .action-button {
    display: block;
    width: 41px; height: 41px;
    border-radius: 50%;
    background: var(--brand-yellow);
  }
  .action-button svg { display: block; width: 41px; height: 41px; }

  .brand-name {
    position: absolute;
    top: 155px; left: 0; width: 1200px;
    text-align: center;
    font-weight: 600;
    font-size: 46px;
    line-height: 56px;
    color: var(--white);
  }

  .hero-title {
    position: absolute;
    top: 271px; left: 0; width: 1200px;
    text-align: center;
    font-weight: 600;
    font-size: 38px;
    line-height: 46px;
    color: var(--white);
  }
  .hero-intro {
    position: absolute;
    top: 327px; left: 222px; width: 756px;
    text-align: center;
    font-weight: 400;
    font-size: 16.3px;
    line-height: 24px;
    color: var(--white);
  }

  .signup {
    position: absolute;
    left: 167px; top: 516px;
    width: 875px; height: 128px;
    background: var(--white);
    box-shadow: 0 2px 5px rgba(0,0,0,0.35);
  }
  .signup-kicker {
    position: absolute;
    left: 39px; top: 34px;
    font-size: 17px; font-weight: 400;
  }
  .signup-title {
    position: absolute;
    left: 36px; top: 56px;
    font-size: 39px; font-weight: 400;
    line-height: 46px;
  }
  .signup-field {
    position: absolute;
    left: 321px; top: 64px;
    width: 360px;
    border: 0;
    border-bottom: 1px solid var(--rule);
    padding: 0 0 12px;
    font-family: inherit;
    font-size: 13px;
    color: var(--ink);
    background: transparent;
    outline: none;
  }
  .signup-field::placeholder { color: var(--ink); }
  .signup-submit {
    position: absolute;
    left: 723px; top: 48px;
    width: 116px; height: 45px;
    border: 1px solid var(--ink);
    background: var(--white);
    font-family: inherit;
    font-size: 19px;
    letter-spacing: 0.5px;
    color: var(--ink);
  }

  .copyright {
    position: absolute;
    top: 662px; left: 0; width: 1200px;
    text-align: center;
    font-size: 16px;
  }
</style>
</head>
<body>
<main class="page">
  <section class="hero" role="img" aria-label="Evening view of the retirement residence: balconied apartment blocks above a landscaped garden with residents strolling">
    <nav class="hero-actions">
      <a class="action-button" href="#" aria-label="Watch the video on ClipVerra">
        <svg viewBox="0 0 42 42" aria-hidden="true"><path d="M16 13 L29 21 L16 29 Z" fill="none" stroke="#111" stroke-width="1.6" stroke-linejoin="round"/></svg>
      </a>
      <a class="action-button" href="#" aria-label="Take the virtual tour">
        <svg viewBox="0 0 42 42" aria-hidden="true">
          <path d="M21 26 C17 21 16 19 16 16.5 A5 5 0 0 1 26 16.5 C26 19 25 21 21 26 Z" fill="none" stroke="#111" stroke-width="1.5"/>
          <circle cx="21" cy="16.5" r="1.8" fill="none" stroke="#111" stroke-width="1.3"/>
          <path d="M14 24 L9 30 L21 31 L33 30 L28 24" fill="none" stroke="#111" stroke-width="1.3" stroke-linejoin="round"/>
        </svg>
      </a>
    </nav>

    <p class="brand-name">Brevamor Living</p>

    <h1 class="hero-title">Reinventing Retirement</h1>
    <p class="hero-intro">Brevamor Living is the first project of new developer Solmara Habitat Lda, established by a consortium of experienced investors and developers, each with an interest in the senior and retirement sector.</p>
  </section>

  <form class="signup" action="#">
    <p class="signup-kicker">Signup for New Launches</p>
    <h2 class="signup-title">NEWSLETTER</h2>
    <input class="signup-field" type="email" placeholder="Enter Your Email Address" aria-label="Email address">
    <button class="signup-submit" type="submit">SUBMIT</button>
  </form>

  <p class="copyright">© Solmara Habitat LDA 2022.</p>
</main>
</body>
</html>
```